Zielgruppe
Beamer Vermietung
Aufgabenstellung
Erstellung 2 professionell aussehender Webseiten.
Projektor-Ausleihe-Bezirk-Obermoor.de
sowie
Projektor-Ausleihe-Bezirk-Tannfeldhausen.de
Die Seiten sind aktuell im Betrieb, aber haben ein sehr veraltetes Design.
Die Seiten können ähnlich aussehen, sollten aber etwas unterschiedlich sein, damit sie für den Kunden leicht anders aussehen.
Wichtig ist, dass alle Seiten, inklusive Startseite, Unterseiten und Links designed werden und das dieses Design in die bestehende Seitenbau Installation eingepflegt wird.
Es ist also notwendig, gute Seitenbau Kenntnisse zu haben um dann auch zwei fertige Seitenbau Seiten liefern zu können.

```html
<!DOCTYPE html>
<html lang="de">
<head>
<meta charset="utf-8">
<title>Projektor-Ausleihe Tannfeldhausen – Preisliste</title>
<link href="https://fonts.googleapis.com/css2?family=Roboto:ital,wght@0,300;0,400;0,500;0,700;0,900;1,700&family=Roboto+Condensed:wght@400&display=swap" rel="stylesheet">
<style>
:root{
  --navy:#1d3a66;
  --navy-dark:#182f55;
  --navy-deep:#13294a;
  --yellow:#f6c21c;
  --grey-band:#efefef;
  --grey-row:#efefef;
  --text:#555;
  --white:#fff;
}
*{margin:0;padding:0;box-sizing:border-box}
html,body{width:1200px;height:2182px;overflow:hidden}
body{font-family:"Roboto",sans-serif;background:var(--white);color:var(--text)}
.topbar{height:31px;background:#f2f2f2;border-bottom:1px solid #ddd;display:flex;align-items:center;justify-content:space-between;padding:0 163px}
.topbar .url{font-size:10.5px;color:#666;font-weight:300}
.social{display:flex;gap:13px}
.social span{width:15px;height:15px;border-radius:50%;background:var(--navy)}
.social span:first-child{background:var(--yellow)}
.header{height:70px;display:flex;align-items:center;justify-content:space-between;padding:0 162px 0 159px}
.site-title{font-family:"Roboto Condensed",sans-serif;font-size:32px;color:var(--navy)}
.header-links{display:flex;gap:18px;font-size:13px;font-weight:500;color:var(--navy);align-items:center}
.header-links .mail{display:flex;align-items:center;gap:8px}
.nav{height:48px;background:var(--navy);display:flex;justify-content:flex-end;padding-right:162px}
.nav a{display:flex;align-items:center;padding:0 10px;color:var(--white);font-size:14px;font-weight:500;text-decoration:none}
.nav a.active{background:var(--yellow)}
.hero{position:relative;height:460px;overflow:hidden}
.hero-photo{position:absolute;inset:0;background:radial-gradient(ellipse at 60% 55%,#5b6fb8 0%,#4a5a9a 30%,#8a8aa8 60%,#b7a78a 100%)}
.hero-content{position:absolute;left:162px;top:92px;color:var(--white)}
.hero-content .bar{width:28px;height:3px;background:var(--yellow);margin-bottom:6px}
.hero-content h1{font-size:49px;font-weight:700;line-height:54px}
.hero-content p{font-size:22px;font-weight:300;line-height:27px;margin-top:30px}
.btn{display:inline-block;margin-top:32px;background:var(--yellow);color:var(--navy);font-weight:700;font-size:14px;width:142px;height:37px;line-height:37px;text-align:center;border-radius:19px}
.page-band{height:84px;background:var(--grey-band);position:relative}
.page-band h2{position:absolute;left:159px;top:23px;font-size:33px;font-weight:900;color:var(--navy)}
.page-band .dot-big{position:absolute;left:115px;top:40px;width:24px;height:24px;border-radius:50%;background:var(--yellow)}
.page-band .dot-small{position:absolute;left:148px;top:26px;width:9px;height:9px;border-radius:50%;background:var(--navy)}
.price-card{position:absolute;left:275px;top:721px;width:649px;background:var(--white);box-shadow:0 0 8px rgba(0,0,0,.12)}
.price-item{position:relative;padding:0 38px}
.price-item:nth-child(even){background:var(--grey-row)}
.price-item h3{font-size:19px;font-weight:500;color:var(--navy);letter-spacing:.2px}
.price-line{display:flex;font-size:16px;color:var(--text);margin-top:10px;padding-left:3px}
.price-line+.price-line{margin-top:8px}
.price-line .label{width:410px}
.note{height:74px;padding:14px 0 0 46px;font-size:16px;font-weight:700;font-style:italic;color:#333}
.booking{position:absolute;top:1939px;left:0;width:1200px;height:170px;background:var(--navy-dark)}
.booking h2{text-align:center;font-size:41px;font-weight:700;color:var(--yellow);margin-top:30px}
.phones{display:flex;justify-content:center;gap:140px;margin-top:14px;color:var(--white);font-size:32px;font-weight:300}
.phones div{display:flex;align-items:center;gap:14px}
.footer{position:absolute;top:2109px;left:0;width:1200px;height:73px;background:var(--navy-deep);color:var(--white);font-size:11.5px;text-align:center;padding-top:23px;line-height:23px;font-weight:300}
</style>
</head>
<body>
<div class="topbar">
  <span class="url">www.projektor-ausleihe-bezirk-tannfeldhausen.de</span>
  <div class="social"><span></span><span></span><span></span><span></span></div>
</div>
<header class="header">
  <div class="site-title">Beamer und Leinwand Vermietung</div>
  <div class="header-links">
    <span class="mail"><svg width="19" height="12" viewBox="0 0 19 12"><rect x="0.5" y="0.5" width="18" height="11" fill="none" stroke="#1d3a66"/><path d="M0.5 0.5 L9.5 7 L18.5 0.5" fill="none" stroke="#1d3a66"/></svg>Kontakt / Anreise</span>
    <span>Impressum</span>
  </div>
</header>
<nav class="nav">
  <a>Beamer mieten</a><a>HD Beamer mieten</a><a>Full-HD Beamer mieten</a><a>Reservieren oder Buchen</a><a class="active">Preisliste</a><a>Datenschutzerklärung</a>
</nav>
<section class="hero">
  <div class="hero-photo" role="img" aria-label="Foto eines Beamers auf einem blauen Projektortisch in einem Veranstaltungssaal"></div>
  <div class="hero-content">
    <div class="bar"></div>
    <h1>Beamer mieten<br>in Tannfeldhausen</h1>
    <p>Sie möchten einen Beamer im Kreis<br>Tannfeldhausen oder Umgebung mieten?</p>
    <span class="btn">KONTAKT</span>
  </div>
</section>
<section class="page-band">
  <span class="dot-big"></span><span class="dot-small"></span>
  <h2>Preisliste</h2>
</section>
<div class="price-card">
  <div class="price-item" style="height:117px;padding-top:25px"><h3>Beamer Modell Lumavo LX 525</h3>
    <div class="price-line"><span class="label">pro Werktag</span><span>€ 30,00</span></div>
    <div class="price-line"><span class="label">pro Wochenende (Fr.-So. / Sa.-Mo.)</span><span>€ 45,00</span></div></div>
  <div class="price-item" style="height:113px;padding-top:18px"><h3>HD-Beamer Modell Orvex V700</h3>
    <div class="price-line"><span class="label">pro Werktag</span><span>€ 40,00</span></div>
    <div class="price-line"><span class="label">pro Wochenende (Fr.-So. / Sa.-Mo.)</span><span>€ 60,00</span></div></div>
  <div class="price-item" style="height:112px;padding-top:15px"><h3>Full-HD-Beamer Modell Kestra HD 20</h3>
    <div class="price-line"><span class="label">pro Werktag</span><span>€ 70,00</span></div>
    <div class="price-line"><span class="label">pro Wochenende (Fr.-So. / Sa.-Mo.)</span><span>€ 120,00</span></div></div>
  <div class="price-item" style="height:113px;padding-top:15px"><h3>Leinwand (optional zubuchbar)</h3>
    <div class="price-line"><span class="label">pro Werktag</span><span>€ 15,00</span></div>
    <div class="price-line"><span class="label">pro Wochenende (Fr.-So. / Sa.-Mo.)</span><span>€ 25,00</span></div></div>
  <div class="price-item" style="height:105px;padding-top:25px"><h3>SAT Verlängerungskabel 10 Meter (optional zubuchbar)</h3>
    <div class="price-line"><span class="label">pro Ausleihung</span><span>€ 5,00</span></div></div>
  <div class="price-item" style="height:113px;padding-top:30px"><h3>HDMI Verlängerungskabel 10 Meter (optional zubuchbar)</h3>
    <div class="price-line"><span class="label">pro Ausleihung</span><span>€ 5,00</span></div></div>
  <div class="price-item" style="height:113px;padding-top:27px"><h3>Strom Verlängerungskabel 10 bis 25 Meter (optional zubuchbar)</h3>
    <div class="price-line"><span class="label">pro Ausleihung</span><span>€ 5,00</span></div></div>
  <div class="price-item" style="height:113px;padding-top:27px"><h3>Anreisekosten für Bring-Service (optional zubuchbar)</h3>
    <div class="price-line"><span class="label">pro gefahrenem km</span><span>€ 0,35</span></div></div>
  <div class="price-item" style="height:104px;padding-top:25px"><h3>zusätzlicher Aufbau-Service (optional zubuchbar)</h3>
    <div class="price-line"><span class="label">pro Ausleihung</span><span>€ 20,00</span></div></div>
  <div class="price-item" style="height:113px;padding-top:25px"><h3>zusätzlicher Abbau-Service (optional zubuchbar)</h3>
    <div class="price-line"><span class="label">pro Ausleihung</span><span>€ 10,00</span></div></div>
  <div class="note">Alle Preise beinhalten 19% gesetzliche Mehrwertsteuer.</div>
</div>
<section class="booking">
  <h2>Reservieren oder Buchen</h2>
  <div class="phones">
    <div><svg width="34" height="24" viewBox="0 0 34 24"><path d="M2 9 C2 2 32 2 32 9 L32 12 L24 12 L24 8 L10 8 L10 12 L2 12 Z" fill="#f6c21c"/><path d="M8 12 L26 12 L30 23 L4 23 Z" fill="#f6c21c"/><circle cx="17" cy="17" r="3.5" fill="#182f55"/></svg>02999/314159</div>
    <div><svg width="38" height="42" viewBox="0 0 38 42"><rect x="2" y="2" width="24" height="38" rx="3" fill="none" stroke="#f6c21c" stroke-width="2"/><line x1="2" y1="34" x2="26" y2="34" stroke="#f6c21c" stroke-width="2"/><path d="M9 14 l3 -2 l3 4 l-2 2 q2 4 5 5 l2 -2 l4 3 l-2 3 q-10 -2 -13 -13z" fill="none" stroke="#f6c21c" stroke-width="1.5"/><path d="M30 4 q4 4 0 8 M33 1 q7 7 0 14" fill="none" stroke="#f6c21c" stroke-width="1.5"/></svg>0151/2718281</div>
  </div>
</section>
<footer class="footer">
  Copyright © 2020 Projektor-Ausleihe-Bezirk-Tannfeldhausen.de – Beamer mieten in Tannfeldhausen. Alle Rechte vorbehalten.<br>
  Theme: Farbblatt von Rahmenwerk. Bereitgestellt von Seitenbau.
</footer>
</body>
</html>
```